Real estate investor, needing a business card that communicates warmth, integrity, empathy.

I have a logo that can be manipulated to align with the message - "Here for every homeowner's next step." Want it to stand out from typical real estate investor cards, and make distressed home sellers feel a connection with me. Should communicate warmth, integrity, empathy, and trustworthiness.

Target Market(s)

Distressed home owners who need to sell their homes, not using realtors.

Contact Information for Business Card

Glossy front and matte back, with a small box that is labelled "notes." I like darker blues and blacks together, but doesn't have to be, as long as it communicates trustworthiness, and a strong call to action.

Other font styles liked:
• see "must haves" above, but willing to review whatever comes my way.

Requirements
Must have
• The fonts on my logo are Aviano, Lusitana, and Marcellus. We don't have to use those, but I favor them.

```html
<!DOCTYPE html>
<html lang="en">
<head>
<meta charset="utf-8">
<title>Harborlight Property Partners – Business Card</title>
<link href="https://fonts.googleapis.com/css2?family=Lusitana:wght@400;700&family=Roboto:wght@400;500&display=swap" rel="stylesheet">
<style>
  :root {
    --stage: #1d1b1c;
    --card-navy: #1a2541;
    --ink-white: #ffffff;
    --ink-soft: #dfe3ec;
  }
  * { box-sizing: border-box; margin: 0; padding: 0; }
  html, body { width: 1200px; height: 1200px; overflow: hidden; }
  body {
    background: var(--stage);
    display: flex;
    flex-direction: column;
    align-items: center;
    justify-content: center;
    gap: 80px;
    font-family: "Roboto", Arial, sans-serif;
    color: var(--ink-white);
  }
  .card {
    position: relative;
    width: 700px;
    height: 400px;
    background: var(--card-navy);
    border-radius: 22px;
    overflow: hidden;
  }

  /* Contact side */
  .holder { position: absolute; left: 48px; top: 52px; }
  .holder-name { font-size: 26px; font-weight: 500; letter-spacing: 0.5px; }
  .holder-title { font-size: 14px; color: var(--ink-soft); margin-top: 2px; }

  .brand-small {
    position: absolute; right: 48px; top: 56px;
    display: flex; align-items: center; gap: 10px;
    font-family: "Lusitana", Georgia, serif; font-size: 24px; font-weight: 400;
  }
  .brand-dot { width: 10px; height: 10px; border-radius: 50%; background: var(--ink-white); flex: none; }

  .contact-list {
    position: absolute; left: 90px; bottom: 44px;
    list-style: none; font-size: 17px; line-height: 1.3;
  }
  .contact-list li { display: flex; align-items: flex-start; gap: 10px; }
  .contact-list svg { width: 14px; height: 14px; margin-top: 4px; flex: none; }

  /* Brand side */
  .brand-large {
    position: absolute; left: 0; right: 0; top: 120px;
    text-align: center;
    font-family: "Lusitana", Georgia, serif;
  }
  .brand-name { font-size: 50px; font-weight: 400; letter-spacing: 0.5px; }
  .brand-tagline {
    font-size: 14px; letter-spacing: 2px; margin-top: 14px; color: var(--ink-soft);
  }
  .notes {
    position: absolute; left: 200px; right: 56px; bottom: 48px;
    display: flex; align-items: flex-end; gap: 14px;
  }
  .notes-label { font-size: 18px; font-weight: 500; letter-spacing: 0.5px; }
  .notes-box { flex: 1; height: 44px; background: var(--ink-white); }
</style>
</head>
<body>

  <section class="card card-contact">
    <div class="holder">
      <p class="holder-name">JONATHAN DOE</p>
      <p class="holder-title">Principal Broker</p>
    </div>

    <div class="brand-small">
      <span class="brand-dot"></span>
      <span>Harborlight Property Partners</span>
    </div>

    <ul class="contact-list">
      <li>
        <svg viewBox="0 0 14 14" aria-hidden="true"><path d="M7 1a4 4 0 0 0-4 4c0 3 4 8 4 8s4-5 4-8a4 4 0 0 0-4-4zm0 5.5A1.5 1.5 0 1 1 7 3.5a1.5 1.5 0 0 1 0 3z" fill="currentColor"/></svg>
        <span>418 Alder Lane<br>Fairbanks, AK 99701</span>
      </li>
      <li>
        <svg viewBox="0 0 14 14" aria-hidden="true"><path d="M3 1l2.5 3-1.3 1.5a8 8 0 0 0 4.3 4.3L10 8.5l3 2.5-1.5 2C6 13 1 8 1 2.5z" fill="currentColor"/></svg>
        <span>907.555.0142</span>
      </li>
      <li>
        <svg viewBox="0 0 14 14" aria-hidden="true"><rect x="3.5" y="1" width="7" height="12" rx="1.2" fill="none" stroke="currentColor" stroke-width="1.4"/></svg>
        <span>907.555.0187</span>
      </li>
      <li>
        <svg viewBox="0 0 14 14" aria-hidden="true"><rect x="1" y="3" width="12" height="8" fill="none" stroke="currentColor" stroke-width="1.3"/><path d="M1 3l6 5 6-5" fill="none" stroke="currentColor" stroke-width="1.3"/></svg>
        <span>hello@harborlightpp.com</span>
      </li>
      <li>
        <svg viewBox="0 0 14 14" aria-hidden="true"><circle cx="7" cy="7" r="5.6" fill="none" stroke="currentColor" stroke-width="1.2"/><path d="M1.4 7h11.2M7 1.4c-3 3-3 8.2 0 11.2M7 1.4c3 3 3 8.2 0 11.2" fill="none" stroke="currentColor" stroke-width="1"/></svg>
        <span>www.harborlightpp.com</span>
      </li>
    </ul>
  </section>

  <section class="card card-brand">
    <div class="brand-large">
      <p class="brand-name">Harborlight Property Partners</p>
      <p class="brand-tagline">- Here for every homeowner's next step -</p>
    </div>
    <div class="notes">
      <span class="notes-label">NOTES</span>
      <div class="notes-box"></div>
    </div>
  </section>

</body>
</html>
```